Pop-up Poster for Expo

We need a design implemented for a Pop-up Poster for a Construction Expo. We have the following concept:

Purpose:
Poster for Exposition to attract people to come to our stand to talk about property management solutions.

Poster Size: see here -> http://www.quillmarkprints.com/item.php?pid=517

Main picture:

attached as layout version - we would like to have the picture as large as possible; change the green/turquoise shirt of the girl in one of our logo’s colors, probably blue is best)

Headline:
One For All

Text under picture:
Complete
Efficient
Visual
Main Logo:

RVT Solutions (on top, maybe as transparent logo in the picture)

Other Logos:

Orvanta Partner (also important, maybe somewhere into the picture)
Birch & Tolvane (can fill the very bottom)

Industry/Entity Type

Construction

```html
<!DOCTYPE html>
<html lang="en">
<head>
<meta charset="utf-8">
<title>RVT Solutions – One For All pop-up poster</title>
<link rel="stylesheet" href="https://fonts.googleapis.com/css2?family=Questrial&display=swap">
<style>
  :root {
    --page-bg: #ffffff;
    --poster-deep: #1768bb;
    --poster-mid: #2f8fd8;
    --poster-light: #66c2ee;
    --white: #ffffff;
    --headline-top: #ffd21c;
    --headline-bottom: #f07a10;
    --silver-top: #ffffff;
    --silver-mid: #c9ced4;
    --silver-bottom: #8e969f;
    --photo-top: #6a5a4c;
    --photo-mid: #7b7d80;
    --photo-low: #2f4e9a;
    --badge: #7cc243;
  }
  * { box-sizing: border-box; margin: 0; padding: 0; }
  html, body {
    width: 1200px; height: 1000px; overflow: hidden;
    background: var(--page-bg);
    font-family: "Questrial", "Century Gothic", sans-serif;
  }
  .canvas { position: relative; width: 1200px; height: 1000px; }

  .poster {
    position: absolute; left: 427px; top: 38px;
    width: 346px; height: 926px; overflow: hidden;
    background: radial-gradient(ellipse 75% 45% at 25% 58%, var(--poster-light) 0%, var(--poster-mid) 45%, var(--poster-deep) 100%);
  }

  .brand { position: absolute; top: 14px; left: 0; right: 0; text-align: center; color: var(--white); }
  .brand-name { font-size: 19px; letter-spacing: 0.5px; line-height: 1; }
  .brand-tagline { font-size: 5px; letter-spacing: 1.5px; text-transform: uppercase; margin-top: 2px; }

  .headline {
    position: absolute; top: 48px; left: 0; right: 0; text-align: center;
    font-size: 50px; line-height: 48px; letter-spacing: 0.5px;
    background: linear-gradient(180deg, var(--headline-top) 0%, var(--headline-bottom) 100%);
    -webkit-background-clip: text; background-clip: text; color: transparent;
    filter: drop-shadow(0 2px 2px rgba(0,0,0,0.25));
  }

  .hero-photo {
    position: absolute; left: 62px; top: 152px; width: 246px; height: 548px;
    border-radius: 110px 110px 20px 20px;
    background: linear-gradient(180deg, var(--photo-top) 0%, var(--photo-mid) 40%, var(--photo-low) 82%, rgba(47,78,154,0) 100%);
    opacity: 0.85;
  }

  .values {
    position: absolute; top: 688px; left: 0; right: 0; text-align: center;
    font-size: 38px; line-height: 44px; letter-spacing: 0.5px;
    background: linear-gradient(180deg, var(--silver-top) 0%, var(--silver-mid) 55%, var(--silver-bottom) 100%);
    -webkit-background-clip: text; background-clip: text; color: transparent;
    filter: drop-shadow(0 2px 2px rgba(0,0,0,0.3));
  }
  .values .line { display: block; }

  .partner { position: absolute; left: 16px; top: 840px; color: var(--white); }
  .partner-badge { display: block; width: 14px; height: 14px; background: var(--badge); margin: 0 0 4px 96px; }
  .partner-name { font-size: 15px; line-height: 1; }
  .partner-level { font-size: 6px; margin: 4px 0 0 62px; }

  .associate { position: absolute; right: 30px; top: 848px; color: var(--white); text-align: center; }
  .associate-tagline { font-size: 5px; letter-spacing: 1.5px; text-transform: uppercase; margin-bottom: 3px; }
  .associate-name { font-size: 18px; line-height: 20px; }
</style>
</head>
<body>
<div class="canvas">
  <main class="poster">
    <header class="brand">
      <div class="brand-name">RVT Solutions</div>
      <div class="brand-tagline">property management</div>
    </header>

    <h1 class="headline">ONE<br>FOR ALL</h1>

    <div class="hero-photo" role="img" aria-label="Photo of a young woman in a grey cardigan, white scarf and blue top, standing with hands in pockets"></div>

    <p class="values">
      <span class="line">COMPLETE</span>
      <span class="line">EFFICIENT</span>
      <span class="line">VISUAL</span>
    </p>

    <footer>
      <div class="partner">
        <span class="partner-badge"></span>
        <div class="partner-name">Orvanta Partner</div>
        <div class="partner-level">Silver Enterprise Resource Planning</div>
      </div>
      <div class="associate">
        <div class="associate-tagline">consulting</div>
        <div class="associate-name">Birch &amp;<br>Tolvane</div>
      </div>
    </footer>
  </main>
</div>
</body>
</html>
```